Occupational Therapist does home accessibility for disabled folks; needs business card design

We need a business card for a company in Portland, Oregon that specializes in making homes accessible, comfortable, and functional for people who are disabled or aging who would like to stay in THEIR home. Our medical background as Occupational Therapists allows us to translate the functional needs of the person into the recommendations for the design of the home remodel.

Target Market(s)

Elderly, children of elderly
People with disabilities, families of people with disabilities

Industry/Entity Type

Business

Contact Information for Business Card

Company name: Stayvale
Name: Karen Dwyer Lopez, OTR/L, CAPS, ECHM
Occupational Therapist, Home Modification & Accessibility Specialist
website: www.stayvaleaccess.com
email: stayvaleaccess@mailbright.com
phone: (503)418-2957
CCB #: 384517

Font styles to use
Sans Serif

Requirements
Must have
• My logo
• Easy to read font with contrasting background
• Please list the Services offered: Occupational Therapy, Home safety & accessibility assessments, Home modification consulting, project management
Nice to have
• Friendly, welcoming feel
Should not have
• Dark colored background

```html
<!DOCTYPE html>
<html lang="en">
<head>
<meta charset="utf-8">
<title>Stayvale Business Card</title>
<link rel="stylesheet" href="https://fonts.googleapis.com/css2?family=Roboto:wght@400;700&family=Roboto+Condensed:wght@400;700&display=swap">
<style>
  :root {
    --bg: #e9e7e3;
    --card: #ffffff;
    --orange: #d9822b;
    --ink: #3a3a3a;
    --grey: #5f5f5f;
  }
  * { box-sizing: border-box; margin: 0; padding: 0; }
  html, body { width: 1200px; height: 900px; overflow: hidden; }
  body {
    background: var(--bg);
    font-family: "Roboto", Arial, sans-serif;
    color: var(--ink);
    position: relative;
  }
  .card {
    position: absolute;
    left: 280px;
    width: 640px;
    height: 366px;
    background: var(--card);
    box-shadow: 0 6px 18px rgba(0,0,0,.18);
    overflow: hidden;
  }
  .card--front { top: 62px; }
  .card--back { top: 472px; }

  /* Brand block */
  .brand {
    position: absolute;
    display: flex;
    align-items: center;
    gap: 16px;
  }
  .brand__mark {
    width: 58px;
    height: 58px;
    background: var(--orange);
  }
  .brand__name {
    font-family: "Roboto Condensed", Arial, sans-serif;
    font-weight: 400;
    color: var(--grey);
    letter-spacing: -1px;
    line-height: 1;
  }

  /* Front: logo + services */
  .card--front .brand { left: 220px; top: 96px; }
  .card--front .brand__name { font-size: 78px; }
  .services {
    position: absolute;
    left: 150px;
    top: 210px;
    font-size: 15px;
    line-height: 1.55;
    color: var(--ink);
  }
  .services__line:nth-child(2) { padding-left: 14px; }
  .front-band {
    position: absolute;
    left: 0; right: 0; bottom: 0;
    height: 20px;
    background: var(--orange);
  }

  /* Back: contact details */
  .person { position: absolute; left: 40px; top: 30px; }
  .person__name {
    font-size: 22px;
    font-weight: 700;
    letter-spacing: .3px;
    text-transform: uppercase;
  }
  .person__name-accent { color: var(--orange); }
  .person__creds {
    font-size: 13px;
    font-weight: 700;
    color: var(--grey);
    margin-top: 2px;
  }
  .person__title {
    font-size: 14px;
    line-height: 1.45;
    color: var(--ink);
    margin-top: 16px;
    padding-left: 18px;
    max-width: 260px;
  }
  .contact {
    position: absolute;
    left: 40px;
    top: 158px;
    list-style: none;
    font-size: 15px;
    color: var(--ink);
  }
  .contact__item {
    display: flex;
    align-items: center;
    gap: 12px;
    height: 26px;
  }
  .contact__item:nth-child(2) { padding-left: 8px; }
  .contact__item:nth-child(3) { padding-left: 16px; }
  .contact__icon { width: 16px; height: 16px; flex: none; }
  .license {
    position: absolute;
    right: 54px;
    top: 150px;
    font-family: "Roboto Condensed", Arial, sans-serif;
    font-weight: 700;
    font-size: 22px;
    color: var(--ink);
    letter-spacing: .5px;
  }
  .card--back .brand { right: 70px; bottom: 36px; }
  .card--back .brand__mark { width: 48px; height: 48px; }
  .card--back .brand__name { font-size: 62px; }
</style>
</head>
<body>

<section class="card card--front" aria-label="Card front">
  <div class="brand">
    <span class="brand__mark"></span>
    <span class="brand__name">Stayvale</span>
  </div>
  <div class="services">
    <p class="services__line">Occupational Therapy | Home safety &amp; accessibility assessments</p>
    <p class="services__line">Home modification consulting | Project management</p>
  </div>
  <div class="front-band"></div>
</section>

<section class="card card--back" aria-label="Card back">
  <div class="person">
    <h1 class="person__name">Karen <span class="person__name-accent">Dwyer Lopez</span></h1>
    <p class="person__creds">OTR/L, CAPS, ECHM</p>
    <p class="person__title">Occupational Therapist, Home Modification &amp; Accessibility Specialist</p>
  </div>

  <ul class="contact">
    <li class="contact__item">
      <svg class="contact__icon" viewBox="0 0 16 16" aria-hidden="true">
        <path fill="#d9822b" d="M3.2 1.5l2.3 2.3-1.3 1.9c.9 2 2.4 3.5 4.3 4.4l1.9-1.3 2.3 2.3-1.4 2.4C6.5 13 3 9.5 1 4.3z"/>
      </svg>
      <span>(503)418-2957</span>
    </li>
    <li class="contact__item">
      <svg class="contact__icon" viewBox="0 0 16 16" aria-hidden="true">
        <rect x="1" y="3" width="14" height="10" fill="#d9822b"/>
        <path d="M1.5 3.8L8 9l6.5-5.2" fill="none" stroke="#fff" stroke-width="1.3"/>
      </svg>
      <span>stayvaleaccess@mailbright.com</span>
    </li>
    <li class="contact__item">
      <svg class="contact__icon" viewBox="0 0 16 16" aria-hidden="true">
        <circle cx="8" cy="8" r="6.5" fill="none" stroke="#d9822b" stroke-width="1.5"/>
        <ellipse cx="8" cy="8" rx="2.6" ry="6.5" fill="none" stroke="#d9822b" stroke-width="1.2"/>
        <path d="M1.5 8h13" stroke="#d9822b" stroke-width="1.2"/>
      </svg>
      <span>www.stayvaleaccess.com</span>
    </li>
  </ul>

  <p class="license">CCB-384517</p>

  <div class="brand">
    <span class="brand__mark"></span>
    <span class="brand__name">Stayvale</span>
  </div>
</section>

</body>
</html>
```